Birch Harbor - Countertop fabricator
Need stationary, business card and T-shirt design
Birch Harbor - Countertop fabricator -
Creative Brief
Simple
Kevin Rasble
14 Larkwood Lane Syracuse, NY13099
info@birchharborny.example
www.birchharborny.example
Back of card to list materials; Granite Quatz Marble Soapstone Solid Surface

```html
<!DOCTYPE html>
<html lang="en">
<head>
<meta charset="utf-8">
<title>Birch Harbor Stationery</title>
<link rel="stylesheet" href="https://fonts.googleapis.com/css2?family=Crimson+Text:wght@400;600&display=swap">
<style>
  :root {
    --bronze: #8d7244;
    --bronze-soft: #e9e2d6;
    --ink: #2e2b27;
    --paper: #ffffff;
    --edge: #d6d2cc;
    --rule: #b9b2a6;
    --ground: #ffffff;
  }
  * { box-sizing: border-box; margin: 0; padding: 0; }
  html, body { width: 1200px; height: 1101px; overflow: hidden; background: var(--ground); }
  body { position: relative; font-family: "Crimson Text", "Times New Roman", serif; color: var(--ink); }

  .sheet { position: absolute; background: var(--paper); border: 1px solid var(--edge); box-shadow: 0 1px 4px rgba(0,0,0,0.12); }

  /* brand lockup */
  .brand { position: absolute; display: flex; flex-direction: column; align-items: flex-start; }
  .brand-square { background: var(--bronze); }
  .brand-name { color: var(--ink); font-weight: 400; letter-spacing: -0.5px; line-height: 1; white-space: nowrap; }

  /* letterhead */
  .letterhead { left: 66px; top: 24px; width: 723px; height: 1011px; }
  .letterhead .brand { left: 24px; top: 102px; }
  .letterhead .brand-square { width: 60px; height: 60px; margin-left: 30px; margin-bottom: 8px; }
  .letterhead .brand-name { font-size: 34px; }
  .letterhead .header-rule { position: absolute; left: 24px; right: 24px; top: 210px; height: 1px; background: var(--rule); }
  .contact { position: absolute; left: 432px; top: 128px; font-size: 12.5px; line-height: 15px; color: var(--ink); }
  .letterhead-accent { position: absolute; left: 414px; top: 936px; width: 300px; height: 75px;
    background: linear-gradient(to bottom, var(--bronze-soft), rgba(233,226,214,0.35)); }

  /* business card front */
  .card-front { left: 825px; top: 24px; width: 345px; height: 195px; }
  .card-front .brand { left: 72px; top: 30px; }
  .card-front .brand-square { width: 32px; height: 32px; margin-left: 16px; margin-bottom: 4px; }
  .card-front .brand-name { font-size: 19px; }
  .card-front .person { position: absolute; right: 30px; top: 92px; font-size: 14px; font-weight: 600; color: var(--bronze); }
  .card-front .card-rule { position: absolute; left: 20px; right: 20px; top: 112px; height: 1px; background: var(--rule); }
  .card-front .card-contact { position: absolute; left: 20px; right: 20px; top: 176px; font-size: 6.5px; color: var(--ink); white-space: nowrap; }

  /* business card back */
  .card-back { left: 825px; top: 225px; width: 345px; height: 195px; background: var(--bronze); border-color: var(--bronze); }
  .materials { position: absolute; left: 150px; top: 48px; list-style: none; color: #f5efe4; font-size: 11px; line-height: 14px; }

  /* envelope */
  .envelope { left: 375px; top: 555px; width: 795px; height: 405px; }
  .envelope .flap { position: absolute; left: 0; top: 0; width: 795px; height: 190px; }
  .envelope .brand { left: 30px; top: 160px; }
  .envelope .brand-square { width: 56px; height: 56px; margin-left: 28px; margin-bottom: 8px; }
  .envelope .brand-name { font-size: 34px; }
  .envelope .header-rule { position: absolute; left: 30px; right: 24px; top: 270px; height: 1px; background: var(--rule); }
  .envelope .return-address { position: absolute; left: 420px; top: 275px; font-size: 12.5px; }
</style>
</head>
<body>

<section class="sheet letterhead" aria-label="Letterhead">
  <div class="brand">
    <span class="brand-square"></span>
    <span class="brand-name">BirchHarbor</span>
  </div>
  <address class="contact" style="font-style:normal">
    14 Larkwood Lane Syracuse, NY13099<br>
    P: 315-555-0142 F: 315-555-0187<br>
    E: info@birchharborny.example<br>
    www.birchharborny.example
  </address>
  <div class="header-rule"></div>
  <div class="letterhead-accent" role="img" aria-label="Faint brand column motif along the lower edge"></div>
</section>

<section class="sheet card-front" aria-label="Business card front">
  <div class="brand">
    <span class="brand-square"></span>
    <span class="brand-name">BirchHarbor</span>
  </div>
  <p class="person">Kevin Rasble</p>
  <div class="card-rule"></div>
  <p class="card-contact">14 Larkwood Lane Syracuse, NY13099 P: 315-555-0142 F: 315-555-0187 info@birchharborny.example</p>
</section>

<section class="sheet card-back" aria-label="Business card back">
  <ul class="materials">
    <li>Granite</li>
    <li>Quatz</li>
    <li>Marble</li>
    <li>Soapstone</li>
    <li>Solid Surface</li>
  </ul>
</section>

<section class="sheet envelope" aria-label="Envelope">
  <svg class="flap" viewBox="0 0 795 190" aria-hidden="true">
    <path d="M0 0 H795 L470 175 Q397 200 325 175 Z" fill="var(--bronze)"/>
  </svg>
  <div class="brand">
    <span class="brand-square"></span>
    <span class="brand-name">BirchHarbor</span>
  </div>
  <div class="header-rule"></div>
  <p class="return-address">14 Larkwood Lane Syracuse, NY13099</p>
</section>

</body>
</html>
```